Design the Business card for NetVaultix

Business card required for a professional Cyber Security business.
Company Logo and Icon has already been provided however I would like other options for the logo and icon to compare to. Alternatively, please refine/enhance the image of the logo.icon I have already provided.

If you are going to use the provided logo and icon, I was thinking that the company raised Logo on White background would serve well on the front of the card. See attached. AND, a large company raised stand-alone icon to appear on black background on the back of the card with tagline 'Cyber Risk Management, Governance and Consulting' or 'Cyber Security for your Business' See attached.
Alternatively, provide your own design for the logo and icon.

Target Market(s)

Enterprise, Government, Financial.

Contact Information for Business Card

Teodor Vaskelin
Founder and CEO

Email Address
Mobile Number
Website URL
LinkedIn URL

Logo Text

NetVaultix - see attached example of logo

Font styles to use
Other font styles liked:
• Berlin Sans FB

Requirements
Must have
• Clean large and bold icon on the back with tagline.
• Horizontal alignment,
Nice to have
• Round edges.
• Raised Logo/Icon
Should not have
• An unprofessional look and feel.

```html
<!DOCTYPE html>
<html lang="en">
<head>
<meta charset="UTF-8">
<title>NetVaultix Business Card</title>
<link rel="stylesheet" href="https://fonts.googleapis.com/css2?family=Quicksand:wght@300;400;500;700&display=swap">
<style>
  :root {
    --bg: #e6e6e6;
    --card: #ffffff;
    --brand-blue: #1f6fb8;
    --text-blue: #3b66b0;
    --accent-yellow: #f5b800;
    --shadow: rgba(0, 0, 0, 0.22);
  }
  * { margin: 0; padding: 0; box-sizing: border-box; }
  html, body {
    width: 1200px;
    height: 1200px;
    overflow: hidden;
    background: var(--bg);
    font-family: "Quicksand", sans-serif;
  }
  .canvas {
    position: relative;
    width: 1200px;
    height: 1200px;
  }
  .card {
    position: absolute;
    left: 260px;
    width: 680px;
    height: 400px;
    background: var(--card);
    border-radius: 34px;
    box-shadow: 0 10px 24px var(--shadow);
  }
  .card-front { top: 150px; }
  .card-back { top: 640px; }

  .brand {
    position: absolute;
    inset: 0;
    display: flex;
    align-items: center;
    justify-content: center;
    gap: 28px;
  }
  .brand-dot {
    width: 120px;
    height: 120px;
    border-radius: 50%;
    background: var(--brand-blue);
  }
  .brand-name {
    font-weight: 700;
    font-size: 78px;
    color: var(--brand-blue);
    letter-spacing: -1px;
  }

  .holder {
    position: absolute;
    left: 56px;
    top: 52px;
  }
  .holder-name {
    font-weight: 500;
    font-size: 34px;
    color: var(--text-blue);
    line-height: 1.15;
  }
  .holder-title {
    font-weight: 300;
    font-size: 22px;
    color: var(--accent-yellow);
    margin-top: 2px;
  }
  .contact-list {
    position: absolute;
    left: 56px;
    bottom: 44px;
    list-style: none;
  }
  .contact-item {
    font-weight: 400;
    font-size: 22px;
    letter-spacing: 3.5px;
    color: var(--text-blue);
    line-height: 42px;
  }
  .back-mark {
    position: absolute;
    right: 60px;
    top: 70px;
    width: 170px;
    height: 170px;
    border-radius: 50%;
    background: var(--text-blue);
  }
</style>
</head>
<body>
  <main class="canvas">
    <section class="card card-front" aria-label="Card front">
      <div class="brand">
        <div class="brand-dot"></div>
        <span class="brand-name">NetVaultix</span>
      </div>
    </section>

    <section class="card card-back" aria-label="Card back">
      <div class="holder">
        <p class="holder-name">Teodor Vaskelin</p>
        <p class="holder-title">Founder and CEO</p>
      </div>
      <div class="back-mark"></div>
      <ul class="contact-list">
        <li class="contact-item">Email Address</li>
        <li class="contact-item">Mobile Number</li>
        <li class="contact-item">Website URL</li>
        <li class="contact-item">LinkedIn URL</li>
      </ul>
    </section>
  </main>
</body>
</html>
```